Business Card design for Property Developer

We need a business card design for a Melbourne based Property Developer called "Kestrelmoor Holdings Pty Ltd".

We subdivide land and onsell to builders etc.

We already have a company logo, which is attached. Also I have attached the layout requirements from the printer. We would like a 2-sided design with one side displaying our logo by itself and the other with the required info, such as name, address, tel no., email, abn etc. The card will need to be used by 4 members of staff so name and contact details should be interchangable.
Updates

If possible, can you please write "name' "job position" "phone" "email" "address" on the card but leave them so I can add the details at a later time. Thank you. Also I plan on printing with UV spot printing as a background on the card. Keep this is mind when designing.

Thanks again.

Hello designers, please do not include pics of houses, house plansĀ or construction machinery etc as we really do not like the way it looks. Thank you.

Target Market(s)

Real Estate Agents, Land Owners, Local Council Departments, Govt Bodies, other Developers etc.

Industry/Entity Type

Business

Requirements
Must have
• 2-sided design with one side displaying our logo by itself and the other with the required info, such as name, address, tel no., email, abn etc.

```html
<!DOCTYPE html>
<html lang="en">
<head>
<meta charset="utf-8">
<title>Kestrelmoor Holdings – Business Card</title>
<link rel="stylesheet" href="https://fonts.googleapis.com/css2?family=Tenor+Sans&family=Montserrat:wght@800&display=swap">
<style>
  :root {
    --stage: #0a0a0a;
    --card-blue: #3a8fe8;
    --card-blue-light: #8fd3fb;
    --ring-cyan: #8ef0ff;
    --rule-navy: #0f2a5c;
    --text-white: #ffffff;
    --label-red: #d8231f;
    --brand-red: #c41e1b;
    --brand-navy: #1b3a9c;
  }
  * { margin: 0; padding: 0; box-sizing: border-box; }
  html, body {
    width: 1200px; height: 700px; overflow: hidden;
    background: var(--stage);
  }
  .stage { position: relative; width: 1200px; height: 700px; }
  .card {
    position: absolute; top: 208px;
    width: 434px; height: 282px; overflow: hidden;
  }
  .card--info { left: 126px; background: var(--card-blue); }
  .card--brand {
    left: 640px;
    background: radial-gradient(ellipse at 48% 42%, var(--card-blue-light) 0%, #5db3f3 45%, var(--card-blue) 100%);
  }
  .info-ring {
    position: absolute; left: 0; top: 0;
    width: 240px; height: 282px;
  }
  .holder-name {
    position: absolute; right: 20px; top: 47px;
    font-family: "Tenor Sans", sans-serif; font-weight: normal;
    font-size: 25px; line-height: 30px;
    letter-spacing: 1.5px; color: var(--text-white);
  }
  .holder-rule {
    position: absolute; left: 234px; right: 0; top: 78px;
    border-top: 2px solid var(--rule-navy);
  }
  .holder-role {
    position: absolute; right: 20px; top: 82px;
    font-family: "Tenor Sans", sans-serif; font-size: 10.5px; font-style: italic;
    letter-spacing: 1px; color: var(--text-white);
  }
  .contact-list {
    position: absolute; left: 238px; top: 131px; list-style: none;
    font-family: "Tenor Sans", sans-serif; font-size: 11px;
    font-variant: small-caps;
    color: var(--text-white); letter-spacing: 0.5px;
  }
  .contact-item { display: flex; line-height: 15px; margin-bottom: 5px; white-space: nowrap; }
  .contact-item--address { margin-bottom: 6px; }
  .contact-label {
    width: 26px; flex: none; font-size: 10px; color: var(--text-white);
    font-variant: normal;
  }
  .contact-label b { color: var(--label-red); font-weight: normal; }
  .brand-lockup {
    position: absolute; left: 0; right: 0; top: 76px;
    display: flex; flex-direction: column; align-items: center; gap: 16px;
  }
  .brand-mark { width: 84px; height: 84px; }
  .brand-name {
    font-family: "Montserrat", sans-serif; font-weight: 800;
    font-size: 20px; letter-spacing: 0.5px; color: var(--brand-red);
  }
</style>
</head>
<body>
<main class="stage">
  <section class="card card--info" aria-label="Card front: contact details">
    <svg class="info-ring" viewBox="0 0 240 282" aria-hidden="true">
      <circle cx="36" cy="140" r="166" fill="none" stroke="var(--ring-cyan)" stroke-width="17"/>
    </svg>
    <h1 class="holder-name">MARLOW</h1>
    <div class="holder-rule"></div>
    <p class="holder-role">GENERAL MANAGER</p>
    <ul class="contact-list">
      <li class="contact-item contact-item--address"><span class="contact-label">[<b>A</b>]</span><span>Harbour Lane 18<br>Oregon, USA</span></li>
      <li class="contact-item"><span class="contact-label">[<b>P</b>]</span><span>+10 482 715 30264</span></li>
      <li class="contact-item"><span class="contact-label">[<b>F</b>]</span><span>+10 482 715 30265</span></li>
      <li class="contact-item"><span class="contact-label">[<b>E</b>]</span><span>marlow@kestrelmoor.com</span></li>
      <li class="contact-item"><span class="contact-label">[<b>W</b>]</span><span>www.kestrelmoor.com</span></li>
    </ul>
  </section>

  <section class="card card--brand" aria-label="Card back: company name">
    <div class="brand-lockup">
      <svg class="brand-mark" viewBox="0 0 84 84" aria-hidden="true">
        <circle cx="42" cy="42" r="40" fill="var(--brand-navy)"/>
      </svg>
      <p class="brand-name">KESTRELMOOR HOLDINGS</p>
    </div>
  </section>
</main>
</body>
</html>
```